FC Morlan - Creation of a AD banner for our yearly event

We are a local soccer club in Switzerland. We're organizing a event that will substitute to our yearly club dinner. We need a banner AD to promote on the social networks this event.
We would like to see design that use one or the 2 colors of the club (blue and red).
This Ad should link to a online shop where we can buy vouchers.

Requirements
Must have
• Logo of the club
Title : Fête des lanternes d'hiver
Call to action : Plus d'informations
Side texte : Grande Tombola
Banner size : W300xH250 or W300xH600
Nice to have
• Promotion texte: Soutenez le FC Morlan et les restaurateurs locaux

```html
<!DOCTYPE html>
<html lang="fr">
<head>
<meta charset="utf-8">
<title>FC Morlan – Bannières Fête des lanternes d'hiver</title>
<link href="https://fonts.googleapis.com/css2?family=Archivo+Black&family=Playfair+Display:wght@800&family=Roboto:wght@400&display=swap" rel="stylesheet">
<style>
  :root{
    --page:#ebebeb;
    --night:#0b0b0c;
    --club-red:#e8233f;
    --club-blue:#0a88cc;
    --grass:#3d7a1c;
    --grass-dark:#24500e;
    --white:#ffffff;
  }
  html,body{margin:0;padding:0;}
  body{width:1200px;height:1000px;overflow:hidden;background:var(--page);position:relative;}

  .banner{
    position:absolute;width:810px;height:675px;overflow:hidden;
    background:var(--night);transform-origin:0 0;
  }
  .banner--large{left:364px;top:163px;}
  .banner--small{left:26px;top:375px;transform:scale(0.37037);}

  .banner__scene{
    position:absolute;inset:0;
    background:
      radial-gradient(ellipse 30% 40% at 95% 45%, rgba(200,20,30,.85), transparent 70%),
      radial-gradient(ellipse 14% 45% at 5% 80%, rgba(200,20,30,.8), transparent 70%),
      linear-gradient(180deg,#0b0b0c 0%,#121212 55%,#1d3a10 66%,var(--grass) 78%,var(--grass-dark) 100%);
  }

  .club-name{
    position:absolute;left:16px;top:16px;
    display:flex;align-items:center;gap:8px;
    font-family:"Archivo Black",sans-serif;font-size:26px;line-height:30px;color:var(--white);
    white-space:nowrap;
  }
  .club-name__dot{width:22px;height:22px;border-radius:50%;background:var(--club-blue);flex:none;}

  .title-frame{
    position:absolute;left:236px;top:12px;width:555px;height:150px;
    border:5px solid var(--club-red);border-bottom:none;box-sizing:border-box;
  }
  .title{
    position:absolute;left:236px;top:30px;width:555px;margin:0;text-align:center;
    font-family:"Playfair Display",serif;font-weight:800;font-size:56px;line-height:74px;
    color:var(--white);
  }

  .tombola{
    position:absolute;left:50px;top:245px;width:810px;margin:0;text-align:center;
    font-family:"Archivo Black",sans-serif;font-size:96px;line-height:112px;
    color:var(--club-red);
    -webkit-text-stroke:7px var(--white);paint-order:stroke fill;
    text-shadow:0 0 14px rgba(255,255,255,.65);
  }
  .pointer{position:absolute;left:430px;top:455px;}

  .cta{
    position:absolute;left:0;top:497px;width:810px;height:80px;
    border-top:6px solid var(--white);border-bottom:6px solid var(--white);
    background:var(--club-red);box-sizing:border-box;
    display:flex;align-items:center;justify-content:center;gap:18px;
    font-family:"Archivo Black",sans-serif;font-size:50px;color:var(--white);
    text-decoration:none;white-space:nowrap;
  }

  .promo{
    position:absolute;left:12px;top:618px;width:790px;height:48px;box-sizing:border-box;
    border:2px solid var(--white);
    display:flex;align-items:center;justify-content:center;
    font-family:"Roboto",sans-serif;font-size:29px;color:var(--white);white-space:nowrap;
  }
</style>
</head>
<body>

<div class="banner banner--small">
  <div class="banner__scene" role="img" aria-label="Photo de joueurs de football sur pelouse avec ruban rouge"></div>
  <div class="club-name"><span class="club-name__dot"></span>FC MORLAN</div>
  <div class="title-frame"></div>
  <h1 class="title">Fête des lanternes<br>d'hiver</h1>
  <p class="tombola">GRANDE<br>TOMBOLA</p>
  <svg class="pointer" width="36" height="22" viewBox="0 0 36 22"><path d="M0 0H36L18 22Z" fill="#fff"/></svg>
  <a class="cta" href="#">
    <svg width="70" height="36" viewBox="0 0 70 36"><path d="M0 0L32 18L0 36Z M36 0L68 18L36 36Z" fill="#fff"/></svg>
    Plus d'informations
    <svg width="70" height="36" viewBox="0 0 70 36"><path d="M34 0L2 18L34 36Z M70 0L38 18L70 36Z" fill="#fff"/></svg>
  </a>
  <div class="promo">Soutenez le FC Morlan et les restaurateurs locaux</div>
</div>

<div class="banner banner--large">
  <div class="banner__scene" role="img" aria-label="Photo de joueurs de football sur pelouse avec ruban rouge"></div>
  <div class="club-name"><span class="club-name__dot"></span>FC MORLAN</div>
  <div class="title-frame"></div>
  <h1 class="title">Fête des lanternes<br>d'hiver</h1>
  <p class="tombola">GRANDE<br>TOMBOLA</p>
  <svg class="pointer" width="36" height="22" viewBox="0 0 36 22"><path d="M0 0H36L18 22Z" fill="#fff"/></svg>
  <a class="cta" href="#">
    <svg width="70" height="36" viewBox="0 0 70 36"><path d="M0 0L32 18L0 36Z M36 0L68 18L36 36Z" fill="#fff"/></svg>
    Plus d'informations
    <svg width="70" height="36" viewBox="0 0 70 36"><path d="M34 0L2 18L34 36Z M70 0L38 18L70 36Z" fill="#fff"/></svg>
  </a>
  <div class="promo">Soutenez le FC Morlan et les restaurateurs locaux</div>
</div>

</body>
</html>
```